Our Pantry Remedy

I am a pharmacist turn chef and my current website www.ourpantryremedy-demo.com is in desperate need of a make over. I want to be able to add how to videos, photographs and have tabs. The tabs needed will be Home, About, Recipes, Health & Wellness, Services, Confidentiality, Affordability, Blog, Articles and Friday Cocktails. Eventually I will want a news letter, but do not want that now, only the ability to add it later. I will also want to add a market place tab later to sell merchandise and ebooks. The ability to navigate should be easy and not confusing and the ability to post should be easy. I will need social media Friendlyn, Clipboardia, searcho plus, searcho, Snapvue and chirpit. In addition I will need some direction on how to operate the site. Examples of website I like (but do not want to copy) are www.buildbrightvigor-demo.net www.drpaulvenmore-demo.com. It is best for me to work with someone who can explain things simply.
Updates

Another website I think is nice is www.zbgalley-demo.com  Thanks!

Target Market(s)

The business will be diving right into the delicious side of Key West’s good health as a personal chef, a culinary wellness coach, a wellness cooking teacher, a healthful caterer and a wellness host and entertainer.
The site needs to promote health with the art of food because I am convinced that health is best enhanced, maintained and recovered through nutritious eating and cuisine, and not through pills.
I will be infusing fresh recipes with a Key West flair in hopes to share my passion and insights into nutrition and health with residents and visitors alike. I want everyone to feel welcome to come in and join the fun.

Industry/Entity Type

Chef

Colors

Designer to choose colors to be used in the design.

Requirements
Must have
• Easy navigation, easy operation and posting and social media tools. Spam filters to keep the creeps away and important plugins that make it all work.
Nice to have
• Everything is nice to have

```html
<!DOCTYPE html>
<html lang="en">
<head>
<meta charset="utf-8">
<title>Our Pantry Remedy</title>
<link href="https://fonts.googleapis.com/css2?family=Source+Sans+3:wght@400;600;700&family=Dancing+Script:wght@500&display=swap" rel="stylesheet">
<style>
:root{
  --green:#25c182;
  --green-dark:#1ea56e;
  --green-deep:#179a63;
  --ink:#3c3c3c;
  --text:#555;
  --muted:#aaa;
  --rule:#e3e3e3;
  --btn:#555;
  --footer:#4a4a4a;
  --white:#fff;
}
*{margin:0;padding:0;box-sizing:border-box}
html,body{width:898px;height:1200px;overflow:hidden;background:var(--white)}
body{position:relative;font-family:"Source Sans 3",Arial,sans-serif;color:var(--ink)}
.abs{position:absolute}

.brand{left:97px;top:16px}
.brand-name{font-size:22px;font-weight:600;color:var(--green);line-height:1}
.brand-tag{font-size:9.5px;font-weight:600;color:#666;margin-top:6px}
.search{left:642px;top:26px;width:133px;height:23px;background:#ececec}
.search svg{position:absolute;right:10px;top:4px}

.nav{left:0;top:76px;width:898px;height:42px;background:var(--green);border-bottom:3px solid var(--green-dark)}
.nav a{position:absolute;top:14px;font-size:10.5px;font-weight:600;color:var(--white);text-decoration:none;white-space:nowrap}

.slider{left:87px;top:134px;width:720px;height:306px;background:#e8e8e8;box-shadow:0 8px 8px -6px rgba(0,0,0,.25)}
.slide{position:absolute;left:5px;top:4px;width:710px;height:296px;background:linear-gradient(100deg,#6b5a4c 0%,#a99b8e 30%,#dcd6cf 55%,#c9a99b 80%,#7d6456 100%)}
.slide-head{position:absolute;left:37px;top:43px;color:var(--white);font-weight:700;text-shadow:0 1px 3px rgba(0,0,0,.4);line-height:1.25}
.slide-head .l1{font-size:25px}
.slide-head .l2{font-size:30px}
.dots{position:absolute;right:20px;bottom:12px;display:flex;gap:6px}
.dots i{width:7px;height:7px;background:var(--white)}
.dots i.on{background:var(--green)}

.welcome{left:93px;top:481px;font-size:16.5px;font-weight:600;color:var(--ink)}
.welcome span{color:var(--green)}
.rule{left:87px;top:509px;width:720px;height:1px;background:var(--rule)}
.intro-photo{left:87px;top:531px;width:190px;height:128px;background:linear-gradient(180deg,#d9dbdc 0%,#9ea3a5 55%,#2d2d2d 80%,#c8b8a5 100%)}
.intro-text{left:298px;top:532px;width:508px;font-size:8.6px;line-height:15px;color:var(--text);text-align:justify}
.intro-text p+p{margin-top:15px}

.promo{left:87px;top:710px;width:720px;height:52px;background:var(--green)}
.promo .book{position:absolute;left:168px;top:9px;width:28px;height:33px;background:#f08a3b;border-radius:2px}
.promo .script{position:absolute;left:217px;top:11px;font-family:"Dancing Script",cursive;font-size:20px;color:var(--white)}
.promo .buy{position:absolute;left:398px;top:11px;width:107px;height:31px;background:var(--green-deep);color:var(--white);font-size:15px;font-weight:600;text-align:center;line-height:31px;border-radius:2px}

.col-head{top:808px;font-size:16.5px;font-weight:600;color:var(--ink);white-space:nowrap}
.col-head span{color:var(--green)}
.col-icon{top:810px}
.thumb{top:852px;width:186px;height:63px;border:2px solid #e5e5e5}
.t-salad{left:111px;background:linear-gradient(90deg,#3a3733,#8f9a7a 45%,#e9e9e5 80%)}
.t-kitchen{left:353px;background:linear-gradient(90deg,#c6c2bb,#d89055 40%,#7d6a58 70%,#2a2a2a)}
.t-veg{left:585px;background:linear-gradient(90deg,#b8463a,#7ba33f 45%,#d23a2c 80%,#f0efe9)}

.card-title{font-family:Arial,sans-serif;font-size:13.5px;font-weight:700;color:#444}
.meta{font-family:Arial,sans-serif;font-size:8.8px;color:var(--muted)}
.meta span{color:var(--green)}
.card-text{font-family:Arial,sans-serif;font-size:9.2px;line-height:14.4px;color:#333;width:170px}
.btn{top:1039px;height:19px;background:var(--btn);color:var(--white);font-family:Arial,sans-serif;font-size:9px;font-weight:700;text-align:center;line-height:19px}

.sub-text{left:589px;top:929px;width:205px;font-size:8.4px;line-height:13px;color:#333}
.sub-input{left:590px;top:964px;width:198px;height:33px;border:1px solid #e3e3e3;border-radius:3px}
.sub-input em{position:absolute;left:11px;top:11px;font-family:Arial,sans-serif;font-size:8.8px;color:var(--muted)}
.sub-go{position:absolute;right:-1px;top:-1px;width:35px;height:33px;background:var(--green);border-radius:0 3px 3px 0}
.sub-go svg{position:absolute;left:14px;top:12px}

.footer{left:0;top:1113px;width:898px;height:87px;background:var(--footer);border-top:6px solid var(--green)}
.f-links{position:absolute;left:91px;top:31px;font-size:8.8px;color:var(--white);white-space:nowrap}
.f-links b{font-weight:400;margin:0 4px}
.f-copy{position:absolute;left:91px;top:50px;font-size:8.8px;color:var(--white)}
.socials{position:absolute;left:600px;top:31px;display:flex;gap:10px;font-size:9px;color:var(--white)}
.socials span{display:flex;align-items:center;gap:3px}
.socials i{width:7px;height:7px;background:var(--green)}
</style>
</head>
<body>

<header>
  <div class="abs brand">
    <div class="brand-name">Our Pantry Remedy</div>
    <div class="brand-tag">Better Nutritional for positive healthy Outcomes</div>
  </div>
  <div class="abs search">
    <svg width="16" height="16" viewBox="0 0 16 16"><circle cx="6" cy="6" r="4.5" fill="none" stroke="#9a9a9a" stroke-width="2"/><line x1="9.5" y1="9.5" x2="15" y2="15" stroke="#9a9a9a" stroke-width="2.5"/></svg>
  </div>
</header>

<nav class="abs nav">
  <a style="left:89px">Home</a>
  <a style="left:146px">About</a>
  <a style="left:203px">Recipes</a>
  <a style="left:268px">Health &amp; Wellness</a>
  <a style="left:382px">Services</a>
  <a style="left:449px">Confidentiality</a>
  <a style="left:545px">Affordability</a>
  <a style="left:630px">Blog</a>
  <a style="left:679px">Articles</a>
  <a style="left:737px">Friday Cocktails</a>
</nav>

<section class="abs slider">
  <div class="slide" role="img" aria-label="Smiling woman preparing fresh vegetables in a bright kitchen">
    <div class="slide-head"><div class="l1">Meet the</div><div class="l2">Mineral in the shadows</div></div>
    <div class="dots"><i class="on"></i><i></i><i></i></div>
  </div>
</section>

<h1 class="abs welcome">Welcome to <span>Our Pantry Remedy</span></h1>
<div class="abs rule"></div>
<div class="abs intro-photo" role="img" aria-label="Home kitchen with a cook at the counter"></div>
<div class="abs intro-text">
  <p>Most likely you are not sitting around wondering or fretting about your magnesium blood level. However, we all need to get to know Magnesium much better and the critical role it plays in our bodies.</p>
  <p>Let’s start with the havoc that this little known mineral can play if it is low. Signs and symptoms of magnesium deficiency include muscle weakness, tremor, muscle spasms, bronchial spasms, asthma, fibromyalgia, poor nail growth, leg cramps, brittleness in bones and high blood pressure. Low magnesium in your brain can make you more prone to migraine headaches, insomnia, anxiety, depression and attention deficit problems. More serious symptoms irregular and spastic contractions and tachycardia or rapid heart rate. The vast majority of Americans, 68%, of all Americans do not get the daily recommended amount of magnesium at 320mg per day for women and 420mg per day for men. 19% don’t even get half the amount recommended.</p>
</div>

<section class="abs promo">
  <div class="book" role="img" aria-label="Cookbook illustration"></div>
  <div class="script">Buy my cooking ebook</div>
  <div class="buy">Buy Now</div>
</section>

<svg class="abs col-icon" style="left:110px" width="28" height="16" viewBox="0 0 28 16"><circle cx="9" cy="4" r="4" fill="#25c182"/><path d="M1 16c0-5 3-7 8-7s8 2 8 7z" fill="#25c182"/><circle cx="20" cy="4" r="3.5" fill="#25c182"/><path d="M15 16c0-5 2-7 5.5-7S28 11 28 16z" fill="#25c182"/></svg>
<h2 class="abs col-head" style="left:146px">About <span>Us</span></h2>
<svg class="abs col-icon" style="left:348px" width="22" height="19" viewBox="0 0 22 19"><path d="M9 0C4 0 0 3 0 7c0 2 1 4 3 5l-1 4 4-3c1 .3 2 .5 3 .5 5 0 9-3 9-6.5S14 0 9 0z" fill="#25c182"/><path d="M19 8c2 1 3 3 3 5 0 1.5-.7 3-2 4l.6 2-3-1.5c-1 .3-2 .5-3 .5-2 0-4-.6-5-2 5 0 9-3.5 9.4-8z" fill="#25c182"/></svg>
<h2 class="abs col-head" style="left:375px">Our Blog <span>Updates</span></h2>
<svg class="abs col-icon" style="left:587px;top:814px" width="19" height="13" viewBox="0 0 19 13"><rect x=".75" y=".75" width="17.5" height="11.5" fill="none" stroke="#25c182" stroke-width="1.5"/><path d="M1 1l8.5 7L18 1M1 12l6-5M18 12l-6-5" fill="none" stroke="#25c182" stroke-width="1.3"/></svg>
<h2 class="abs col-head" style="left:614px">Subscribe <span>News Letter</span></h2>

<div class="abs thumb t-salad" role="img" aria-label="Fresh salad being tossed in a glass bowl"></div>
<div class="abs thumb t-kitchen" role="img" aria-label="Cook chopping fruit in a kitchen"></div>
<div class="abs thumb t-veg" role="img" aria-label="Peppers, tomatoes and fresh greens"></div>

<h3 class="abs card-title" style="left:112px;top:927px">All About OPR</h3>
<p class="abs card-text" style="left:112px;top:957px">Lorem ipsum dolor sit amet, consectetur adipiscing elit. Praesent tempor facilisis congue. Lorem sum dolor sit amet, consectetur adippend...</p>
<a class="abs btn" style="left:113px;width:66px">Learn More</a>

<h3 class="abs card-title" style="left:354px;top:928px">My First Creation</h3>
<div class="abs meta" style="left:354px;top:947px">Posted in <span>lena marsh</span> on April 13th, 2014</div>
<p class="abs card-text" style="left:354px;top:972px">Lorem ipsum dolor sit amet, consectetur adipiscing elit. Praesent tempor facilisis congue. Suspend...</p>
<a class="abs btn" style="left:349px;width:87px">Leave a comment</a>
<a class="abs btn" style="left:448px;width:65px">Read More</a>

<p class="abs sub-text">Enter your email address below to subscribe. You will receive our newsletter once a week.</p>
<div class="abs sub-input"><em>enter your email address</em>
  <div class="sub-go"><svg width="6" height="9" viewBox="0 0 6 9"><path d="M1 1l3.5 3.5L1 8" fill="none" stroke="#fff" stroke-width="1.8"/></svg></div>
</div>

<footer class="abs footer">
  <div class="f-links">Home<b>|</b>About<b>|</b>Recipes<b>|</b>Health &amp; Wellness<b>|</b>Services<b>|</b>Confidentiality<b>|</b>Affordability<b>|</b>Blog<b>|</b>Articles<b>|</b>Friday Cocktails</div>
  <div class="f-copy">© Copy Right 2014 &nbsp;Our Pantry Remedy . All Rights Reserved.</div>
  <div class="socials"><span><i></i>Friendlyn</span><span><i></i>Clipboardia</span><span><i></i>searcho plus</span><span><i></i>Snapvue</span></div>
</footer>

</body>
</html>
```